Website Design - Photo Shop Design - Functional Cash Register Layout for POS System

Design a webpage for Point of Sale site. A cash register page.

Page must have a good look. I have attached a file of a possible layout example - but need a much nicer design. I have also attached the site logo. which i will upload without background tomorrow hopefully.

Looking for a nice Fresh look , not dark and dingy.

Target Market(s)

Business

Industry/Entity Type

Business Software

Number of Pages Required

1 page

Colors
f59195
f04a50
ec1f27
fbd4d5
ffffff
f8f3f8
fdf0f6
feeeee
ecf5f6

Requirements
Must have
• Cash register layout for POS software site. Nice layout ,
Nice to have
• Try putting he register part on the left side as well as the right - invert the designs have them different to the layout example shown too.
Should not have
• Not to dark

```html
<!DOCTYPE html>
<html lang="en">
<head>
<meta charset="utf-8">
<title>TillNest – Cash Register</title>
<link href="https://fonts.googleapis.com/css2?family=Arimo:wght@400;700&display=swap" rel="stylesheet">
<style>
  :root{
    --rose-top:#f59195;
    --red:#f04a50;
    --blush:#feeeee;
    --line:#f59195;
    --tile-border:#d6d6d6;
    --ink:#111111;
    --white:#ffffff;
  }
  *{box-sizing:border-box;margin:0;padding:0}
  html,body{width:1200px;height:601px;overflow:hidden;background:var(--white);font-family:"Arimo",Arial,sans-serif}
  .register{position:relative;width:1200px;height:601px}
  .top-band{position:absolute;left:0;top:0;width:1200px;height:22px;background:var(--rose-top)}
  .sidebar{position:absolute;left:0;top:22px;width:168px;height:579px;background:var(--blush)}
  .nav{list-style:none;position:absolute;left:16px;top:47px;width:136px}
  .nav li{height:37px;display:flex;align-items:center;border-bottom:1px solid #f6c9cb;padding-left:18px;gap:6px;
    color:var(--red);font-size:8.5px;font-weight:700;letter-spacing:.1px}
  .nav li:last-child{border-bottom:none}
  .nav svg{width:11px;height:11px;fill:var(--red);flex:none}
  .brand{position:absolute;left:186px;top:58px;display:flex;align-items:center;gap:8px}
  .brand-mark{width:26px;height:26px;border-radius:50%;background:var(--red)}
  .brand-name{font-size:26px;font-weight:700;color:var(--red);letter-spacing:-.5px;line-height:1}
  .brand-sub{position:absolute;left:320px;top:86px;font-size:5px;color:#777}
  .brand-rule{position:absolute;left:186px;top:102px;width:642px;height:1px;background:var(--line)}
  .store-label{position:absolute;right:26px;top:37px;font-size:14px;color:var(--ink)}
  .products{position:absolute;left:186px;top:139px;display:grid;grid-template-columns:repeat(6,96px);column-gap:13.4px;row-gap:17px}
  .tile{width:96px;height:96px;border:2px solid var(--tile-border);background:var(--white);padding:6px}
  .tile span{display:block;width:100%;height:100%;background:linear-gradient(160deg,#e6e6e6,#9a9a9a)}
  .category-bar{position:absolute;left:187px;top:480px;width:646px;height:38px;background:var(--red);display:flex;align-items:center;color:var(--white);
    font-size:11.5px;font-weight:700;letter-spacing:1.6px}
  .category-bar .seg{height:100%;display:flex;align-items:center;padding:0 10px;border-right:1px solid #f68b8f}
  .category-bar .seg:last-of-type{border-right:none}
  .category-bar svg{width:12px;height:20px;stroke:var(--white);stroke-width:2;fill:none}
  .category-bar .next{margin-left:auto;padding-right:12px}
  .cart{position:absolute;left:851px;top:64px;width:321px}
  .cart-head{height:38px;background:var(--red);display:flex;color:var(--white);font-size:12px}
  .customer{flex:1;display:flex;align-items:center;gap:5px;padding-left:8px}
  .customer svg{width:15px;height:18px;fill:var(--white)}
  .txn{width:100px;border-left:1px solid #f68b8f;text-align:right;padding:7px 10px 0 0;line-height:13px}
  .cart-body{position:relative;height:374px;background:var(--blush)}
  .add-notes{position:absolute;left:19px;top:306px;color:var(--red);font-size:12px}
  .totals{position:absolute;left:0;width:100%;top:343px;text-align:center;font-size:7.5px;color:var(--ink)}
  .actions{position:absolute;left:851px;top:486px;width:321px;height:27px}
  .plus{position:absolute;left:0;top:0;width:25px;height:27px;background:var(--blush);color:var(--red);font-size:19px;text-align:center;line-height:25px}
  .park{position:absolute;left:29px;top:0;width:136px;height:27px;background:var(--blush);color:var(--red);font-size:11px;display:flex;align-items:center;justify-content:center}
  .pay{position:absolute;left:183px;top:0;width:138px;height:27px;background:var(--red);color:var(--white);font-size:11px;font-weight:700;display:flex;align-items:center;justify-content:space-between;padding:0 11px 0 16px}
  .keypad-area{position:absolute;left:851px;top:521px;width:321px;height:80px;background:var(--blush)}
</style>
</head>
<body>
<div class="register">
  <div class="top-band"></div>

  <aside class="sidebar">
    <ul class="nav">
      <li><svg viewBox="0 0 12 12"><path d="M6 1 0 6h2v5h3V8h2v3h3V6h2z"/></svg>ENTER SALE</li>
      <li><svg viewBox="0 0 12 12"><path d="M5 0h2v5h2L6 8 3 5h2zM0 8h2v2h8V8h2v4H0z"/></svg>PARKED / LAYBY ORDERS</li>
      <li><svg viewBox="0 0 12 12"><path d="M0 1h1v11H0zM2 2h10L9 5l3 3H2z"/></svg>COMPLETED SALES</li>
      <li><svg viewBox="0 0 12 12"><path d="M1 2h10v10H1zM2 5v6h8V5zM3 0h1v3H3zM8 0h1v3H8z"/></svg>APPOINTMENTS</li>
      <li><svg viewBox="0 0 12 12"><circle cx="6" cy="3.5" r="3"/><path d="M1 12c0-4 2-5 5-5s5 1 5 5z"/></svg>BACK OFFICE</li>
      <li><svg viewBox="0 0 12 12" fill="none" stroke="#f04a50" stroke-width="1.6"><path d="M10 4A4.5 4.5 0 0 0 2 5M2 8a4.5 4.5 0 0 0 8-1"/><path d="M10 1v3H7M2 11V8h3"/></svg>REFRESH DATA</li>
    </ul>
  </aside>

  <div class="brand"><span class="brand-mark"></span><span class="brand-name">TillNest</span></div>
  <div class="brand-sub">powered by Nimbus</div>
  <div class="brand-rule"></div>

  <div class="store-label">My Shop/Cash Register 1</div>

  <section class="products">
    <div class="tile"><span role="img" aria-label="Product photo: spray bottle"></span></div>
    <div class="tile"><span role="img" aria-label="Product photo: camera"></span></div>
    <div class="tile"><span role="img" aria-label="Product photo: monitor"></span></div>
    <div class="tile"><span role="img" aria-label="Product photo: filter cartridge"></span></div>
    <div class="tile"><span role="img" aria-label="Product photo: striped t-shirt"></span></div>
    <div class="tile"><span role="img" aria-label="Product photo: wallet"></span></div>
    <div class="tile"><span role="img" aria-label="Product photo: floor sweeper"></span></div>
    <div class="tile"><span role="img" aria-label="Product photo: snack bag"></span></div>
    <div class="tile"><span role="img" aria-label="Product photo: jacket"></span></div>
    <div class="tile"><span role="img" aria-label="Product photo: phone case"></span></div>
    <div class="tile"><span role="img" aria-label="Product photo: wristbands"></span></div>
    <div class="tile"><span role="img" aria-label="Product photo: bottle of spirits"></span></div>
  </section>

  <nav class="category-bar">
    <div class="seg"><svg viewBox="0 0 12 20"><path d="M10 2 2 10l8 8"/></svg>&nbsp;&nbsp;LIST</div>
    <div class="seg">ALL</div>
    <div class="seg">DEATS</div>
    <div class="seg">UNCATEGORIZED</div>
    <svg class="next" viewBox="0 0 12 20"><path d="M2 2l8 8-8 8"/></svg>
  </nav>

  <section class="cart">
    <div class="cart-head">
      <div class="customer"><svg viewBox="0 0 15 18"><circle cx="7.5" cy="5" r="4.5"/><path d="M0 18c0-6 3-8 7.5-8S15 12 15 18z"/></svg>Select Customer</div>
      <div class="txn">Transaction#<br>00016</div>
    </div>
    <div class="cart-body">
      <div class="add-notes">Add Nates</div>
      <div class="totals">Subtotal: $0.00 | Tax: $0.00 | Disc: | Total: $0.00 Paid: $0.00</div>
    </div>
  </section>

  <div class="actions">
    <div class="plus">+</div>
    <div class="park">SAVE &amp; PARK / LAYBY</div>
    <div class="pay"><span>PAY</span><span>$ 0.00</span></div>
  </div>

  <div class="keypad-area"></div>
</div>
</body>
</html>
```